Business Card Design Project

I am a new business offering a consulting service in Homeware buying, product development and trend forecasting. I would like to use colours that are current and on trend now. Needs to be eye catching, speak of creativity and design.

Front: Matt charcoal card with black gloss embossing name print
Back: white with Pink text

Pink pantone: 812c

Target Market(s)

Retailers and Wholesalers of Homeware products

Industry/Entity Type

Business

Requirements
Must have
• Please go to this link and the card on this link is what I am looking for.

http://www.foliorama.net/gallery/Blank_sheet-KX/402817

1. Card Front

Name on front of card: MARGOT FINCHLEY

2. Back card

The following text must be designed onto the card:

Address: 17 Walloway Street ,Paddington, 2021, NSW, Sydney, Australia
Mobile: +61 (0)412305718
Email: finchmel@wirrolink.net.au

Homeware trends
Product development and sourcing
Strategic Buying management
Nice to have
• Creativity in selection of font, composition and proportion.
Should not have
• I don't want to see graphics/shapes on the card.

```html
<!DOCTYPE html>
<html lang="en">
<head>
<meta charset="utf-8">
<title>Margot Finchley — Business Card</title>
<link rel="stylesheet" href="https://fonts.googleapis.com/css2?family=Arimo:wght@400;700&display=swap">
<style>
  :root {
    --page-bg: #ece9e6;
    --card-black: #0c0c0c;
    --card-edge: #e5336f;
    --emboss: #1b1b1b;
    --emboss-light: #262626;
    --pink-text: #e5336f;
  }
  * { box-sizing: border-box; margin: 0; padding: 0; }
  html, body {
    width: 1200px;
    height: 1000px;
    overflow: hidden;
    background: var(--page-bg);
    font-family: "Arimo", Arial, sans-serif;
  }
  .card-spread {
    position: absolute;
    left: 70px;
    top: 350px;
    display: flex;
    gap: 20px;
  }
  .card {
    position: relative;
    width: 520px;
    height: 300px;
    background: radial-gradient(ellipse at 55% 30%, #161616 0%, var(--card-black) 70%);
    border: 3px solid var(--card-edge);
    box-shadow: 0 6px 16px rgba(0,0,0,0.25);
  }
  /* Front */
  .front-name {
    position: absolute;
    right: 28px;
    top: 30px;
    text-align: right;
    font-weight: 700;
    font-size: 60px;
    line-height: 0.95;
    letter-spacing: 1px;
    color: var(--emboss);
    text-shadow: -1px -1px 0 var(--emboss-light), 1px 1px 1px #050505;
  }
  /* Back */
  .back-details {
    position: absolute;
    left: 80px;
    top: 92px;
    color: var(--pink-text);
    font-size: 11.5px;
    line-height: 1.3;
  }
  .back-name {
    font-weight: 700;
    font-size: 13px;
    margin-bottom: 8px;
  }
  .address { padding-left: 2px; margin-bottom: 10px; }
  .address span { display: block; }
  .contact-row { display: flex; gap: 12px; }
  .contact-label { width: 8px; }
  .services {
    position: absolute;
    left: 80px;
    right: 18px;
    bottom: 28px;
    color: var(--pink-text);
    font-size: 9.5px;
    white-space: nowrap;
  }
  .services .sep { margin: 0 6px; }
</style>
</head>
<body>
  <div class="card-spread">
    <section class="card card-front">
      <h1 class="front-name">MARGOT<br>FINCHLEY</h1>
    </section>
    <section class="card card-back">
      <div class="back-details">
        <div class="back-name">Margot Finchley</div>
        <div class="address">
          <span>17 Walloway Street</span>
          <span>Paddington, 2021</span>
          <span>NSW, Sydney</span>
          <span>Australia</span>
        </div>
        <div class="contact-row"><span class="contact-label">m</span><span>+61 (0)412305718</span></div>
        <div class="contact-row"><span class="contact-label">e</span><span>finchmel@wirrolink.net.au</span></div>
      </div>
      <div class="services">
        Homeware Trends<span class="sep">•</span>Product Development &amp; Sourcing<span class="sep">•</span>Strategic Buying Management
      </div>
    </section>
  </div>
</body>
</html>
```